Gadri Management - Managing Urban Projects for the City of Modiin

Gadri Management needs a website that projects its professionalism and innovation to the residents of the city of Modiin. The design needs include: 1) a homepage design, 2) ~12 customized icons used on the homepage, 3) a layered image (city landscape with company logo on it) used as a fullwidth background image on the homepage. The client wants a site that is pleasant on the eye and easy to navigate. The client wants the site to project the organization as being professional and innovative.

Target Market(s)

adult residents of the city of modiin, israel

Industry/Entity Type

management of urban projects

Number of Pages Required

1 page

Font styles to use
Sans Serif

Requirements
Must have
• psd of design and psd of main fullwidth background image on the homepage
Nice to have
• icons for navigation bar and homepage teasers
Should not have
• colors should match the logo attached, font should be modern

```html
<!DOCTYPE html>
<html lang="en">
<head>
<meta charset="utf-8">
<title>Gadri Management</title>
<link href="https://fonts.googleapis.com/css2?family=Poppins:wght@400;500&display=swap" rel="stylesheet">
<style>
:root{
  --green:#3f9a1e;
  --green-dark:#2b7a1a;
  --green-deep:#1f6b2e;
  --white:#ffffff;
  --ink:#111111;
  --muted:#8a8a8a;
  --field:#ffffff;
}
*{box-sizing:border-box;margin:0;padding:0}
html,body{width:1200px;height:3370px;overflow:hidden}
body{position:relative;font-family:'Poppins',sans-serif;background:#fff;color:var(--ink)}
h2,h3,h4{font-weight:400}
/* sidebar */
.sidebar{position:absolute;left:1034px;top:0;width:166px;height:3370px;background:var(--green)}
.nav-item{position:absolute;left:0;width:166px;border-bottom:1px solid rgba(255,255,255,.25);color:#fff;text-align:center;font-size:23px;line-height:27px;display:flex;flex-direction:column;align-items:center;justify-content:center;gap:14px}
.nav-item svg{width:120px;height:110px;fill:none;stroke:#fff;stroke-width:5;stroke-linecap:round;stroke-linejoin:round}
/* hero */
.hero{position:absolute;left:0;top:0;width:1034px;height:987px;background:linear-gradient(180deg,#7f9bb0 0%,#a6a39a 18%,#8a8677 30%,#56614a 55%,#3a4a35 75%,#2a3325 100%)}
.brand{position:absolute;left:417px;top:70px;width:200px;text-align:center;color:var(--green);font-weight:500;font-size:22px;background:#fff;padding:20px 10px;border-radius:4px;display:flex;align-items:center;gap:10px;justify-content:center}
.brand .dot{width:16px;height:16px;border-radius:50%;background:var(--green);flex:none}
.teaser{position:absolute;top:373px;width:202px;height:268px;background:rgba(63,160,30,.78);border:2px solid rgba(255,255,255,.55);border-radius:14px 14px 0 0;color:#fff;text-align:center;font-size:22px;line-height:26px;padding-top:44px}
.teaser svg{position:absolute;left:46px;top:110px;width:110px;height:110px;fill:none;stroke:#fff;stroke-width:5;stroke-linecap:round;stroke-linejoin:round}
.quote{position:absolute;left:75px;top:718px;width:740px;color:#fff;font-size:38px;line-height:45px}
.cite{position:absolute;left:77px;top:877px;color:#fff;font-size:24px}
.down{position:absolute;left:484px;top:916px}
/* about */
.about-card{position:absolute;left:63px;top:1076px;width:949px;height:492px;background:#fff;border-radius:36px 0 36px 0;box-shadow:0 4px 14px rgba(0,0,0,.18)}
.about-photo{position:absolute;left:73px;top:1087px;width:931px;height:471px;border-radius:36px 0 36px 0;background:linear-gradient(180deg,#3e4a3a 0%,#2f3a2d 45%,#3c3f3b 75%,#4a4c4a 100%)}
.about-title{position:absolute;left:73px;top:1155px;width:931px;text-align:center;color:#fff;font-size:50px;font-weight:400}
.rule{position:absolute;height:3px;background:var(--green)}
.about-text{position:absolute;left:125px;top:1258px;width:825px;text-align:center;color:#fff;font-size:13px;line-height:27px}
.about-text p+p{margin-top:27px}
.btn-green{position:absolute;background:var(--green-dark);border:2px solid #fff;color:#fff;border-radius:40px;text-align:center;font-size:15px}
/* projects */
.projects{position:absolute;left:0;top:1675px;width:1034px;height:750px;background:linear-gradient(135deg,#3d9a1c 0%,#2f8e2a 55%,#2a9a3a 100%)}
.sec-title{position:absolute;width:1034px;left:0;text-align:center;font-size:64px;font-weight:400}
.proj-card{position:absolute;top:1925px;width:276px;height:391px;background:var(--green);border:2px solid #fff;border-radius:0 0 32px 32px;overflow:hidden;color:#fff;text-align:center}
.proj-card .pic{height:210px}
.proj-card h3{font-weight:500;font-size:23px;line-height:27px;margin-top:28px}
.proj-card .more{display:inline-block;margin-top:22px;width:137px;height:42px;line-height:38px;border:2px solid #fff;border-radius:30px;font-size:13px}
.arrow{position:absolute;top:2092px;width:36px;height:56px;fill:none;stroke:#fff;stroke-width:5}
/* contact */
.field{position:absolute;background:var(--field);box-shadow:0 2px 8px rgba(0,0,0,.12);font-size:13px;color:var(--muted);padding-left:42px;line-height:46px}
.field svg{position:absolute;left:20px;top:17px;width:11px;height:12px;fill:#aaa}
.submit{position:absolute;left:475px;top:2891px;width:156px;height:46px;border-radius:30px;background:var(--green-deep);color:#fff;font-size:13px;text-align:center;line-height:46px}
/* footer */
.footer{position:absolute;left:0;top:2988px;width:1034px;height:382px;background:linear-gradient(135deg,#2f8e2a 0%,#3b9f2e 100%)}
.f-head{position:absolute;top:3060px;color:#fff;font-size:18px;font-weight:500}
.f-rule{position:absolute;top:3090px;width:32px;height:2px;background:#fff}
.f-text{position:absolute;color:#fff;font-size:13px;line-height:22px}
.f-contact{position:absolute;left:408px;color:#fff;font-size:13px;line-height:16px;padding-left:45px}
.f-contact .ic{position:absolute;left:0;top:0;width:28px;height:28px;border:1.5px solid #fff;border-radius:4px}
.f-contact svg{position:absolute;left:7px;top:7px;width:14px;height:14px;fill:#fff}
.links{position:absolute;top:3125px;color:#fff;font-size:13px;line-height:27px;list-style:none}
.links li{padding-left:22px;position:relative}
.links li::before{content:"";position:absolute;left:2px;top:10px;width:8px;height:8px;border-radius:50%;border:1.5px solid #fff}
.bottom-bar{position:absolute;left:0;top:3320px;width:1034px;height:50px;background:#277a25}
.copyright{position:absolute;left:0;top:3337px;width:1034px;text-align:center;color:#fff;font-size:12px}
.social{position:absolute;top:3333px;width:29px;height:29px;border:1.5px solid #fff;border-radius:3px}
.to-top{position:absolute;left:76px;top:3318px;width:44px;height:44px;border-radius:50%;background:var(--green);border:2px solid #fff}
</style>
</head>
<body>

<section class="hero" role="img" aria-label="Aerial view of a city with residential buildings, a park and a lake"></section>
<div class="brand"><span class="dot"></span>Gadri Management</div>

<div class="teaser" style="left:102px">Tenders
  <svg viewBox="0 0 110 110"><circle cx="55" cy="18" r="10"/><path d="M38 48a17 12 0 0 1 34 0z"/><circle cx="20" cy="68" r="10"/><path d="M3 98a17 12 0 0 1 34 0z"/><circle cx="90" cy="68" r="10"/><path d="M73 98a17 12 0 0 1 34 0z"/><path d="M55 52v14M55 66l-16 14M55 66l16 14"/></svg>
</div>
<div class="teaser" style="left:326px">Projects
  <svg viewBox="0 0 110 110"><path d="M20 90A48 48 0 1 1 90 90"/><path d="M35 40l10-10 35 35-5 15-15 5z"/><path d="M40 45l30 30"/></svg>
</div>
<div class="teaser" style="left:548px;padding-top:40px">Business<br>Promotion
  <svg viewBox="0 0 110 110" style="top:120px"><path d="M8 40h16l26-14v44L24 56H8z"/><path d="M14 56l6 24h8l-4-24"/><circle cx="75" cy="22" r="14"/><circle cx="85" cy="52" r="14"/><circle cx="72" cy="84" r="14"/><path d="M69 28l12-12M85 44v16M66 84h12"/></svg>
</div>
<div class="teaser" style="left:772px">Video Projects
  <svg viewBox="0 0 110 110"><circle cx="55" cy="55" r="42" stroke-width="7"/><path d="M45 35l28 20-28 20z" fill="#fff"/></svg>
</div>

<p class="quote">Change is the law of life. Those who only look at the&nbsp; Past and the present will surely miss the future.</p>
<p class="cite">(Jonathan F. Kessler)</p>
<svg class="down" width="110" height="72" viewBox="0 0 110 72"><path d="M0 72L55 2l55 70z" fill="#fff"/><rect x="45" y="30" width="20" height="34" rx="10" fill="none" stroke="#888" stroke-width="1.5"/><path d="M55 38v16M50 49l5 5 5-5" fill="none" stroke="#666" stroke-width="1.5"/></svg>

<div class="about-card"></div>
<div class="about-photo" role="img" aria-label="Roundabout and road with a park and buildings in the background, darkened"></div>
<h2 class="about-title">About Gadri Manager</h2>
<div class="rule" style="left:443px;top:1224px;width:193px"></div>
<div class="about-text">
  <p>Gadri Management is the professional body that manages, oversees and accompanies urban projects for the benefit of the public in the city of Givat Lavan.</p>
  <p>The director is responsible for the management of the technology park (Harel), the Lotem center (Orpro), the Shaked park, the municipal sports center including the municipal pool, the transportation center, the municipal signage and more.</p>
</div>
<div class="btn-green" style="left:441px;top:1422px;width:196px;height:60px;line-height:56px">READ MORE</div>

<section class="projects"></section>
<h2 class="sec-title" style="top:1762px;color:#fff">Our Projects</h2>
<div class="rule" style="left:441px;top:1855px;width:195px;background:#fff"></div>

<svg class="arrow" style="left:36px" viewBox="0 0 36 56"><path d="M32 4L6 28l26 24"/></svg>
<svg class="arrow" style="left:996px" viewBox="0 0 36 56"><path d="M4 4l26 24L4 52"/></svg>

<div class="proj-card" style="left:93px">
  <div class="pic" role="img" aria-label="Technology park with lake, lawns and office buildings" style="background:linear-gradient(180deg,#9aa4a6 0%,#8c9a86 45%,#5d8a3c 75%,#4a7e34 100%)"></div>
  <h3>The Technology<br>Park</h3><span class="more">READ MORE</span>
</div>
<div class="proj-card" style="left:400px">
  <div class="pic" role="img" aria-label="Transportation center bridge with palm trees" style="background:linear-gradient(180deg,#c9d3da 0%,#b9b8a8 45%,#8a8a64 70%,#4e6a36 100%)"></div>
  <h3>The Transportation<br>Center</h3><span class="more">READ MORE</span>
</div>
<div class="proj-card" style="left:708px">
  <div class="pic" role="img" aria-label="Indoor municipal swimming pool" style="background:linear-gradient(180deg,#a9b1b6 0%,#7f8790 40%,#5f7b92 70%,#3f6f9a 100%)"></div>
  <h3>The Municipal<br>Sports Center</h3><span class="more">READ MORE</span>
</div>

<h2 class="sec-title" style="top:2496px;color:#111">Contact Us</h2>
<div class="rule" style="left:448px;top:2585px;width:194px;background:#2b8a2a"></div>

<div class="field" style="left:253px;top:2637px;width:294px;height:46px"><svg viewBox="0 0 11 12"><circle cx="5.5" cy="3" r="3"/><path d="M0 12a5.5 5 0 0 1 11 0z"/></svg>First Name</div>
<div class="field" style="left:556px;top:2637px;width:296px;height:46px"><svg viewBox="0 0 11 12"><rect y="2" width="11" height="8"/></svg>E-Mail</div>
<div class="field" style="left:253px;top:2703px;width:294px;height:46px"><svg viewBox="0 0 11 12"><rect x="2" width="7" height="12" rx="1"/></svg>Phone Number</div>
<div class="field" style="left:556px;top:2703px;width:296px;height:46px"><svg viewBox="0 0 11 12"><path d="M5.5 12L1.5 5a4 4 0 1 1 8 0z"/></svg>Address</div>
<div class="field" style="left:253px;top:2772px;width:599px;height:91px"><svg viewBox="0 0 11 12"><circle cx="5.5" cy="6" r="5.5"/></svg>Message</div>
<div class="submit">SUBMIT NOW</div>

<footer class="footer"></footer>
<h4 class="f-head" style="left:76px">About Us</h4><div class="f-rule" style="left:76px"></div>
<h4 class="f-head" style="left:408px">Contact Us</h4><div class="f-rule" style="left:408px"></div>
<h4 class="f-head" style="left:686px">Quick Links</h4><div class="f-rule" style="left:686px"></div>
<p class="f-text" style="left:76px;top:3122px;width:300px">Gadri Management is the professional body that manages, oversees and accompanies urban projects for the benefit of the public in the city of Givat Lavan.</p>

<div class="f-contact" style="top:3128px"><span class="ic"><svg viewBox="0 0 14 14"><path d="M3 1l3 3-2 2a8 8 0 0 0 4 4l2-2 3 3-2 2C5 13 1 9 1 3z"/></svg></span>CALL US<br>08-5550123</div>
<div class="f-contact" style="top:3175px"><span class="ic"><svg viewBox="0 0 14 14"><rect x="3" y="1" width="8" height="4"/><rect x="1" y="5" width="12" height="6"/><rect x="3" y="9" width="8" height="4"/></svg></span>FAX US<br>08-5550144</div>
<div class="f-contact" style="top:3222px"><span class="ic"><svg viewBox="0 0 14 14"><path d="M7 14L2 6a5 5 0 1 1 10 0z"/></svg></span>Cedar Grove 12,<br>Givat Lavan</div>

<ul class="links" style="left:686px">
  <li>Home</li><li>About</li><li>Business Promotion</li><li>Project Management</li><li>Tech and Commercial<br>Areas</li>
</ul>
<ul class="links" style="left:897px">
  <li>Tenders</li><li>Signage and<br>Publication</li><li>Projects</li><li>Contact</li>
</ul>

<div class="bottom-bar"></div>
<div class="to-top"><svg width="40" height="40" viewBox="0 0 40 40" fill="none" stroke="#fff" stroke-width="3"><path d="M12 22l8-8 8 8M12 30l8-8 8 8"/></svg></div>
<p class="copyright">Copyright © 2024 All Rights Reserved By Company name</p>
<span class="social" style="left:877px"></span>
<span class="social" style="left:912px"></span>
<span class="social" style="left:947px"></span>
<span class="social" style="left:982px"></span>

<nav class="sidebar">
  <div class="nav-item" style="top:0;height:334px">
    <svg viewBox="0 0 120 110"><path d="M10 55L60 8l50 47"/><path d="M22 45v58h26V70h24v33h26V45"/></svg>Home</div>
  <div class="nav-item" style="top:334px;height:323px">
    <svg viewBox="0 0 120 110"><path d="M30 100l6-22A50 45 0 1 1 52 92z"/><circle cx="60" cy="28" r="6"/><path d="M55 44h10v38H55z"/></svg>About</div>
  <div class="nav-item" style="top:657px;height:327px">
    <svg viewBox="0 0 120 110"><path d="M6 42h18l28-16v48L24 58H6z"/><path d="M12 58l6 26h8l-4-26"/><circle cx="86" cy="22" r="16"/><circle cx="98" cy="56" r="16"/><circle cx="84" cy="90" r="16"/><path d="M78 30l16-16M98 46v20M77 90h14"/></svg>Business<br>Promotion</div>
  <div class="nav-item" style="top:984px;height:368px">
    <svg viewBox="0 0 120 110"><circle cx="36" cy="55" r="14"/><circle cx="36" cy="55" r="26" stroke-dasharray="10 6"/><rect x="88" y="4" width="24" height="26" rx="3"/><rect x="88" y="42" width="24" height="26" rx="3"/><rect x="88" y="80" width="24" height="26" rx="3"/><path d="M94 17l5 5 8-10M94 55l5 5 8-10M62 55h26"/></svg>Project<br>Management</div>
  <div class="nav-item" style="top:1352px;height:399px">
    <svg viewBox="0 0 120 110"><path d="M10 12l30-8 30 10 30-8v90l-30 8-30-10-30 8z"/><path d="M40 4v92M70 14v92"/><circle cx="94" cy="48" r="20"/><path d="M86 56l6-14 10-2-6 14z"/></svg>Tech and<br>Commercial<br>Areas</div>
  <div class="nav-item" style="top:1751px;height:317px">
    <svg viewBox="0 0 120 110"><circle cx="60" cy="18" r="12"/><path d="M40 52a20 14 0 0 1 40 0z"/><circle cx="22" cy="70" r="12"/><path d="M2 104a20 14 0 0 1 40 0z"/><circle cx="98" cy="70" r="12"/><path d="M78 104a20 14 0 0 1 40 0z"/><path d="M60 56v16M60 72l-16 16M60 72l16 16"/></svg>Tenders</div>
  <div class="nav-item" style="top:2068px;height:369px">
    <svg viewBox="0 0 120 110"><rect x="18" y="30" width="84" height="56"/><path d="M6 92h108l-6 10H12z"/><path d="M44 40h14l20-12v32L58 48H44z"/><path d="M50 48l3 14h6"/></svg>Signage and<br>Publication</div>
  <div class="nav-item" style="top:2437px;height:370px">
    <svg viewBox="0 0 120 110"><path d="M22 96A50 50 0 1 1 98 96"/><path d="M40 40l10-10 38 38-6 16-16 6z"/><path d="M45 45l33 33"/></svg>Projects</div>
  <div class="nav-item" style="top:2807px;height:563px;border-bottom:none;justify-content:flex-start;padding-top:90px">
    <svg viewBox="0 0 120 110"><path d="M30 8l16 18-10 12a50 50 0 0 0 28 28l12-10 18 16-10 14C44 90 16 60 16 22z" fill="#fff"/><path d="M66 22a26 26 0 0 1 24 24M68 6a42 42 0 0 1 38 38"/></svg>Contact</div>
</nav>

</body>
</html>
```